Luxury Face Oil Label

I'm looking for a simple and sophisticated design for a natural face oil that will target the luxe market. It is a pure Natural product. I have attached the logo, Velumi Organics.

Here's the Copy

LUXE FACIAL OIL

Regenerate. Hydrate. Glow

100% Natural

30ml (1.01 oz)

A complex blend of Pure Oils including Marula, Sea Buckthorn, Rosehip, Neroli, Evening primrose, Argan, Calendula, Lavender, Jojoba, Grapeseed, Baobab, Moringa and Vitamin E oil.

Produced by
Brasso Kettle Ltd
P.O box 7925-00300
Nairobi, Kenya
www.velumiorganics.example

Target Market(s)

High end

Requirements
Must have
• Simple, Please consider the bottle, which is a 30ml clear glass bottle with a gold and white pump. Image attached.
Nice to have
• Very clean designs, not too much going on.
Should not have
• Leaves and nuts.

```html
<!DOCTYPE html>
<html lang="en">
<head>
<meta charset="utf-8">
<title>Luxe Facial Oil – Label</title>
<link href="https://fonts.googleapis.com/css2?family=Jost:wght@300;400;500&family=Pinyon+Script&display=swap" rel="stylesheet">
<style>
  :root {
    --page: #ffffff;
    --label: #ececec;
    --olive: #a9ab8b;
    --olive-soft: #c4c5ad;
    --ink: #242424;
    --ink-soft: #3a3a3a;
  }
  * { box-sizing: border-box; margin: 0; padding: 0; }
  html, body { width: 1200px; height: 1200px; overflow: hidden; background: var(--page); }
  body { font-family: "Jost", sans-serif; color: var(--ink); position: relative; }

  .label {
    position: absolute;
    top: 330px;
    width: 540px;
    height: 540px;
    background: var(--label);
  }
  .label--front { left: 45px; }
  .label--back { left: 615px; }

  .rule-top, .rule-bottom {
    position: absolute; left: 0; right: 0; height: 3px; background: var(--olive);
  }
  .rule-top { top: 0; }
  .rule-bottom { bottom: 0; }

  /* front */
  .brand {
    position: absolute; top: 110px; left: 0; right: 0;
    display: flex; align-items: center; justify-content: center; gap: 14px;
  }
  .brand__mark { width: 12px; height: 12px; border: 1.5px solid var(--olive); }
  .brand__name {
    font-weight: 400; font-size: 26px; letter-spacing: 0.28em; color: var(--ink-soft);
  }
  .product-title {
    position: absolute; top: 262px; left: 0; right: 0; text-align: center;
    font-weight: 500; font-size: 36px; letter-spacing: 0.12em; color: var(--ink);
  }
  .title-rule {
    position: absolute; top: 318px; left: 82px; right: 82px; height: 3px; background: var(--olive);
  }
  .benefits {
    position: absolute; top: 334px; left: 0; right: 0; text-align: center;
    font-weight: 300; font-size: 27px; color: var(--ink-soft);
  }
  .dot {
    position: absolute; top: 392px; left: 50%; width: 9px; height: 9px; margin-left: -4.5px;
    border-radius: 50%; background: var(--ink);
  }
  .natural {
    position: absolute; top: 402px; left: 0; right: 0; text-align: center;
    font-family: "Pinyon Script", cursive; font-size: 36px; color: var(--olive);
  }
  .natural-rule {
    position: absolute; top: 452px; left: 50%; width: 60px; margin-left: -30px; height: 2px; background: var(--ink);
  }
  .volume {
    position: absolute; top: 462px; left: 0; right: 0; text-align: center;
    font-weight: 400; font-size: 19px; color: var(--ink);
  }

  /* back */
  .side-rule {
    position: absolute; top: 0; bottom: 0; left: 60px; width: 4px; background: var(--olive-soft);
  }
  .back-copy {
    position: absolute; left: 90px; top: 50px; width: 300px;
    font-weight: 300; font-size: 19.5px; line-height: 30px; color: var(--ink);
  }
  .back-divider { width: 130px; height: 2px; background: var(--olive); margin: 22px 0 16px; }
  .maker { font-weight: 300; font-size: 19.5px; line-height: 30px; color: var(--ink); }
</style>
</head>
<body>
  <section class="label label--front" aria-label="Front label">
    <div class="rule-top"></div>
    <div class="brand">
      <span class="brand__mark"></span>
      <span class="brand__name">VELUMI ORGANICS</span>
    </div>
    <h1 class="product-title">LUXE FACIAL OIL</h1>
    <div class="title-rule"></div>
    <p class="benefits">· Regenerate · Hydrate · Glow ·</p>
    <span class="dot"></span>
    <p class="natural">100% Natural</p>
    <div class="natural-rule"></div>
    <p class="volume">30ml (1.01 oz)</p>
    <div class="rule-bottom"></div>
  </section>

  <section class="label label--back" aria-label="Back label">
    <div class="rule-top"></div>
    <div class="side-rule"></div>
    <div class="back-copy">
      <p>A complex blend of Pure Oils including Marula, Sea Buckthorn, Rosehip, Neroli, Evening primrose, Argan, Calendula, Lavender, Jojoba, Grapeseed, Baobab, Moringa and Vitamin E oil.</p>
      <div class="back-divider"></div>
      <p class="maker">Produced by<br>Brasso Kettle Ltd<br>P.O box 7925-00300<br>Nairobi, Kenya<br>www.velumiorganics.example</p>
    </div>
    <div class="rule-bottom"></div>
  </section>
</body>
</html>
```